Lumo Brew Premium Matcha brand Label

This is a label design project for a luxury tea brand. Feel free to be creative within the guidelines.
Attached to this project is a document called “Private Label Design Requirements” with the design guidelines and template. There is another document called "Lumo Brew Packaging Instructions" this has more details necessary to stick to the guidelines in the first document.

I have also attached the certifications to be included as well as different variations of the logo for you to use.

If you have any questions, I am here.
Updates

Target Market(s)

Young, active, fun, enjoy the finer things

```html
<!DOCTYPE html>
<html lang="en">
<head>
<meta charset="utf-8">
<title>Lumo Brew Matcha Label Variations</title>
<link href="https://fonts.googleapis.com/css2?family=Fira+Sans:wght@400;500;600;700&family=Yanone+Kaffeesatz:wght@400;500&family=Marcellus&display=swap" rel="stylesheet">
<style>
  :root {
    --board: #bab8b9;
    --mint: #edf6e6;
    --cream: #f3f7ea;
    --white: #ffffff;
    --leaf: #6fbf48;
    --leaf-soft: #cfe8c0;
    --ink: #3d3d3d;
    --dark: #222222;
    --gold: #e4dc1f;
    --teal: #5bc6c9;
    --badge-green: #3f9a3c;
    --badge-ring: #2c6f2f;
  }
  * { margin: 0; padding: 0; box-sizing: border-box; }
  html, body { width: 1200px; height: 1054px; overflow: hidden; background: var(--board); }
  body { position: relative; font-family: "Fira Sans", sans-serif; color: var(--ink); }

  .label { position: absolute; left: 148px; width: 903px; height: 153px; overflow: hidden; }
  .label--mint { top: 107px; background: var(--mint); }
  .label--cream { top: 323px; background: var(--cream); }
  .label--white { top: 538px; background: var(--white); }
  .label--green { top: 754px; width: 906px; background: linear-gradient(90deg, var(--leaf) 0%, var(--leaf) 22%, #eaf4e2 45%, #eaf4e2 55%, var(--leaf) 78%, var(--leaf) 100%); }

  .pattern { position: absolute; top: 0; height: 100%; }
  .pattern--cream { left: 218px; width: 435px; background: radial-gradient(ellipse at center, #dcefcf 0%, #eef6e6 55%, var(--cream) 100%); }
  .pattern--white { left: 212px; width: 600px; background: linear-gradient(90deg, #ffffff 0%, #f1f5ec 30%, #f4f7ef 70%, #ffffff 100%); }
  .pattern--green { left: 212px; width: 480px; background: radial-gradient(ellipse at center, #f4f9ef 0%, #e3f1d8 45%, #a8d88b 80%, rgba(111,191,72,0) 100%); }

  .maker { position: absolute; left: 38px; top: 84px; font-size: 7px; line-height: 10px; color: var(--ink); }
  .maker strong { font-weight: 600; display: block; }
  .label--green .maker { left: 43px; top: 64px; color: var(--white); }

  .front { position: absolute; left: 299px; width: 305px; top: 0; height: 100%; text-align: center; }
  .brand-dot { position: absolute; left: 140px; top: 18px; width: 26px; height: 26px; border-radius: 50%; background: var(--leaf); }
  .brand-name { position: absolute; left: 0; right: 0; top: 55px; font-size: 10px; font-weight: 700; color: var(--dark); }
  .brand-box { position: absolute; left: 130px; top: 19px; width: 46px; height: 46px; background: var(--dark); }
  .brand-box .brand-name { top: 31px; font-size: 7.5px; color: var(--white); }
  .label--green .brand-box { left: 128px; width: 50px; height: 49px; }
  .label--green .brand-box .brand-name { top: 34px; }

  .grade { position: absolute; left: 0; right: 0; top: 75px; font-family: "Yanone Kaffeesatz", sans-serif; font-size: 15px; letter-spacing: 0.6px; color: var(--dark); }
  .grade::before, .grade::after { content: ""; display: inline-block; width: 11px; height: 1.5px; background: var(--leaf); vertical-align: middle; margin: 0 3px; }
  .label--green .grade::before, .label--green .grade::after { background: var(--dark); }
  .label--white .grade { top: 70px; font-size: 12px; }

  .product { position: absolute; left: -30px; right: -30px; top: 82px; font-family: "Marcellus", serif; font-size: 49px; line-height: 49px; letter-spacing: 1px; color: var(--leaf); }
  .product--gold { color: var(--gold); -webkit-text-stroke: 0.7px var(--leaf); }
  .label--white .product { top: 78px; font-size: 37px; line-height: 37px; color: var(--dark); }
  .label--green .product { top: 81px; font-size: 50px; }

  .variety { position: absolute; left: 0; right: 0; top: 113px; font-family: "Yanone Kaffeesatz", sans-serif; font-weight: 500; font-size: 13px; letter-spacing: 0.5px; color: var(--leaf); }

  .weight { position: absolute; left: 0; right: 0; top: 131px; font-size: 9.5px; color: var(--ink); }
  .label--white .weight { top: 131px; }
  .label--green .weight { top: 128px; }

  .info { position: absolute; left: 689px; top: 15px; width: 200px; }
  .info h3 { font-size: 10px; font-weight: 400; color: #555; }
  .info h4 { margin-top: 5px; font-size: 11px; font-weight: 500; line-height: 10px; color: #555; }
  .info .rule { width: 40px; height: 1.5px; background: var(--teal); margin-top: 2px; }
  .info ul { list-style: none; margin-top: 3px; }
  .info li { font-size: 8.8px; line-height: 11.6px; letter-spacing: 0.2px; color: #555; }
  .info li::before { content: "•"; margin-right: 5px; font-size: 7px; }
  .label--green .info { left: 692px; top: 15px; }
  .label--green .info h3, .label--green .info h4, .label--green .info li { color: var(--white); }
  .label--green .info .rule { background: var(--dark); margin-top: 12px; }
  .label--green .info ul { margin-top: 12px; }

  .seals { display: flex; align-items: center; gap: 5px; margin-top: 2px; }
  .maker .seals { margin-top: 13px; }
  .seal-square { width: 42px; height: 29px; background: var(--badge-green); }
  .seal-circle { width: 30px; height: 30px; border-radius: 50%; background: var(--badge-green); border: 2px solid #7a3b1c; }
  .seals p { font-size: 8.3px; font-weight: 700; line-height: 10px; color: #555; text-transform: uppercase; }
  .label--green .seals p { color: var(--white); }
</style>
</head>
<body>

<section class="label label--mint">
  <div class="maker">Distributed by Lumo Brew Co. | Ashford, Ga<strong>Certified Organic by Verda Cert</strong><strong>PRODUCT OF JAPAN</strong></div>
  <div class="front">
    <span class="brand-dot"></span><span class="brand-name">Lumo Brew</span>
    <div class="grade">Premium Organic Ceremonial</div>
    <div class="product product--gold">MATCHA</div>
    <div class="weight">Net Wt: 30g (1.06oz)</div>
  </div>
  <div class="info">
    <h3>Ingredients</h3>
    <h4>Premium Organic Japanese Matcha Green Tea</h4>
    <div class="rule"></div>
    <ul><li>2 tsp of Matcha</li><li>2oz of Water (170-180 degrees F)</li><li>Whisk in a W formation until frothy</li><li>Sweeten to taste</li></ul>
    <div class="seals"><span class="seal-square"></span><span class="seal-circle"></span><p>Keep refrigerated<br>for quality”</p></div>
  </div>
</section>

<section class="label label--cream">
  <div class="pattern pattern--cream" role="img" aria-label="Soft white blossom pattern with two pale tea leaves framing the title"></div>
  <div class="maker">Distributed by Lumo Brew Co. | Ashford, Ga<strong>Certified Organic by Verda Cert</strong><strong>PRODUCT OF JAPAN</strong></div>
  <div class="front">
    <span class="brand-dot"></span><span class="brand-name">Lumo Brew</span>
    <div class="grade">Premium Organic Ceremonial</div>
    <div class="product">MATCHA</div>
    <div class="weight">Net Wt: 30g (1.06oz)</div>
  </div>
  <div class="info">
    <h3>Ingredients</h3>
    <h4>Premium Organic Japanese Matcha Green Tea</h4>
    <div class="rule"></div>
    <ul><li>2 tsp of Matcha</li><li>2oz of Water (170-180 degrees F)</li><li>Whisk in a W formation until frothy</li><li>Sweeten to taste</li></ul>
    <div class="seals"><span class="seal-square"></span><span class="seal-circle"></span><p>Keep refrigerated<br>for quality”</p></div>
  </div>
</section>

<section class="label label--white">
  <div class="pattern pattern--white" role="img" aria-label="Faint white blossom pattern across the label"></div>
  <div class="maker">Distributed by Lumo Brew Co. | Ashford, Ga<strong>Certified Organic by Verda Cert</strong><strong>PRODUCT OF JAPAN</strong></div>
  <div class="front">
    <div class="brand-box"><span class="brand-name">Lumo Brew</span></div>
    <div class="grade">Premium Organic Ceremonial</div>
    <div class="product">MATCHA</div>
    <div class="variety">Green Tea</div>
    <div class="weight">Net Wt: 30g (1.06oz)</div>
  </div>
  <div class="info">
    <h3>Ingredients</h3>
    <h4>Premium Organic Japanese Matcha Green Tea</h4>
    <div class="rule"></div>
    <ul><li>2 tsp of Matcha</li><li>2oz of Water (170-180 degrees F)</li><li>Whisk in a W formation until frothy</li><li>Sweeten to taste</li></ul>
    <div class="seals"><span class="seal-square"></span><span class="seal-circle"></span><p>Keep refrigerated<br>for quality”</p></div>
  </div>
</section>

<section class="label label--green">
  <div class="pattern pattern--green" role="img" aria-label="White blossoms and large green tea leaves framing the title"></div>
  <div class="maker">Distributed by Lumo Brew Co. | Ashford, Ga<strong>Certified Organic by Verda Cert</strong><strong>PRODUCT OF JAPAN</strong>
    <div class="seals"><span class="seal-square"></span><span class="seal-circle"></span><p>Keep refrigerated<br>for quality”</p></div>
  </div>
  <div class="front">
    <div class="brand-box"><span class="brand-name">Lumo Brew</span></div>
    <div class="grade">Premium Organic Ceremonial</div>
    <div class="product">MATCHA</div>
    <div class="weight">Net Wt: 30g (1.06oz)</div>
  </div>
  <div class="info">
    <h3>Ingredients</h3>
    <h4>Premium Organic Japanese Matcha Green Tea</h4>
    <div class="rule"></div>
    <ul><li>2 tsp of Matcha</li><li>2oz of Water (170-180 degrees F)</li><li>Whisk in a W formation until frothy</li><li>Sweeten to taste</li></ul>
  </div>
</section>

</body>
</html>
```